SEO Company Needs a Professional, Bold Business Card Design

Kelvo SEO
2487 N Harlow Ave #315
Austin, TX 78705
512-555-0184
http://www.kelvoseo-demo.com
Kelvo SEO is an internet marketing company specializing in SEO for higher-end businesses. We are looking for a professional and bold (edgy) design that communicates our forward thinking SEO strategies. Our typical client is a small to medium US business that has never had SEO work done on their website but does has active marketing. We want our business card design to instill confidence in our services through a professional and bold look. We we would also like the design elements to be in line with the services we offer - ranking client websites in the search engine results, namely Zarnix.
Design Specifics:
Card design should have square edges.
Design should be delivered in fully layered and editable PSD file. Designing in AI is fine but I need a PSD file in case we have any changes in contact information or need additional cards for employees.
The design should compliment the attached logo.
Company Name:
Kelvo SEO
Address:
2487 N Harlow Ave #315
Austin, TX 78705
Personal Info:
Dorian Welk
Owner
theboss@kelvoseo-demo.com
Phone:
877-555-0139 (KELVO UP)
Website:
http://www.kelvoseo-demo.com
Slogan:
Could Your Website Be Generating More Business?
Target Market(s)
High-end business owners - doctors, lawyers, specialists, business owners doing 250k in profit.
Industry/Entity Type
Internet
Contact Information for Business Card
Company Name:
Kelvo SEO
Address:
2487 N Harlow Ave #315
Austin, TX 78705
Personal Info:
Dorian Welk
Owner
theboss@kelvoseo-demo.com
Phone:
877-555-0139 (KELVO UP)
Website:
www.kelvoseo-demo.com
Slogan:
Requirements
Must have
- Card design should have square edges.
- Background should be WHITE only.
- Design should be delivered in fully layered and editable PSD file. Designing in AI is fine but I need a PSD file in case we have any changes in contact information or need additional cards for employees.

```html
<!DOCTYPE html>
<html lang="en">
<head>
<meta charset="utf-8">
<title>Kelvo SEO Business Card</title>
<link rel="stylesheet" href="https://fonts.googleapis.com/css2?family=Open+Sans:ital,wght@0,400;0,600;0,700;1,400&display=swap">
<style>
  :root {
    --stage: #ececec;
    --card: #ffffff;
    --navy: #0f2a4e;
    --blue: #1a8fd6;
    --ink: #1d2a3a;
    --rule: #c9d0d8;
  }
  * { box-sizing: border-box; margin: 0; padding: 0; }
  html, body { width: 1200px; height: 908px; overflow: hidden; }
  body {
    background: var(--stage);
    font-family: "Open Sans", Arial, sans-serif;
    position: relative;
  }
  .card {
    position: absolute;
    top: 305px;
    width: 520px;
    height: 297px;
    background: var(--card);
    box-shadow: 0 2px 10px rgba(0,0,0,0.12);
    overflow: hidden;
  }
  .card--front { left: 50px; }
  .card--back { left: 630px; }

  .brand {
    display: flex;
    align-items: center;
    gap: 10px;
    color: var(--navy);
    font-weight: 700;
    white-space: nowrap;
  }
  .brand__dot {
    width: 16px; height: 16px;
    border-radius: 50%;
    background: var(--blue);
  }
  .card--front .brand {
    position: absolute;
    left: 0; right: 0; top: 96px;
    justify-content: center;
    font-size: 44px;
  }
  .slogan {
    position: absolute;
    left: 0; right: 0; top: 172px;
    text-align: center;
    color: var(--blue);
    font-size: 15px;
  }

  .card--back .brand {
    position: absolute;
    right: 34px; top: 40px;
    font-size: 34px;
  }
  .holder {
    position: absolute;
    left: 30px; top: 96px;
    width: 200px;
    text-align: right;
  }
  .holder__name { color: var(--navy); font-weight: 700; font-size: 17px; line-height: 22px; }
  .holder__role { color: var(--blue); font-style: italic; font-size: 12px; line-height: 16px; }

  .contact {
    position: absolute;
    left: 248px; top: 118px;
    border-left: 1px solid var(--rule);
    padding-left: 12px;
    list-style: none;
    color: var(--ink);
    font-size: 12.5px;
    line-height: 19px;
  }
  .contact li { display: flex; align-items: center; gap: 8px; white-space: nowrap; }
  .contact svg { width: 10px; height: 10px; fill: var(--navy); flex: none; }
  .address {
    position: absolute;
    left: 240px; top: 178px;
    color: var(--ink);
    font-size: 12.5px;
    line-height: 19px;
    white-space: nowrap;
  }
  .bands { position: absolute; left: 0; bottom: 0; width: 520px; height: 60px; }
</style>
</head>
<body>
  <section class="card card--front">
    <div class="brand"><span class="brand__dot"></span>Kelvo SEO</div>
    <p class="slogan">Could Your Website Be Generating More Business?</p>
  </section>

  <section class="card card--back">
    <div class="brand"><span class="brand__dot"></span>Kelvo SEO</div>
    <div class="holder">
      <p class="holder__name">Dorian Welk</p>
      <p class="holder__role">Owner</p>
    </div>
    <ul class="contact">
      <li><svg viewBox="0 0 10 10"><path d="M2 0h2l1 3-1.5 1a6 6 0 0 0 2.5 2.5L7 5l3 1v2c0 1-1 2-2 2A8 8 0 0 1 0 2c0-1 1-2 2-2z"/></svg>877-555-0139 (KELVO UP)</li>
      <li><svg viewBox="0 0 10 10"><path d="M0 2h10v6H0zM0 2l5 3.5L10 2v1L5 6.5 0 3z"/></svg>theboss@kelvoseo-demo.com</li>
      <li><svg viewBox="0 0 10 10"><circle cx="5" cy="5" r="5"/></svg>www.kelvoseo-demo.com</li>
    </ul>
    <p class="address">2487 N Harlow Ave #315 Austin, TX 78705</p>
    <svg class="bands" viewBox="0 0 520 60" aria-hidden="true">
      <polygon points="0,8 300,8 316,30 0,30" fill="var(--navy)"/>
      <polygon points="300,30 520,44 520,52 316,38" fill="var(--blue)"/>
    </svg>
  </section>
</body>
</html>
```